New Automotive supply business in need of label designs for additive range

I need front and back label design for about 12 different variety of products. They are all to do with the Automotive additive industry such as Petrol injector cleaner, Engine Flush, Oil treatments etc. I will provide overall measurements of the label in the brief as well as examples of artwork that I like. Label must comply with local regulations, i can assist you with this. We will start with one product only, and if successful I am happy to hire you to do the remainder of the project. I would like to see designs that use my company logo colors. These products are for the workshop industry only (not retail) so does not have to be too animated.You will see my logo designs under the name "torlux" in the uploaded files.Product Name is : Motor Clear & Renew
Front Label must say:PREPARES ENGINES FOR NEW OIL
RESTORES COMPRESSION
MINIMISES CONTAMINATION WITH NEW OIL
CONTAINS TORLUX ARMOR COAT PROTECTION
RECOMMENDED FOR PETROL, DIESEL AND HYBRID ENGINES
350ML
Dimensions of metal can that will be used for label is : 175mm in height and 56mm in diameter. IN THE UPLOADED FILES YOU WILL SEE A SAMPLE OF THE ACTUAL CAN TO BE USED.
I have now included an example of a shield/guard that should be shown on the rear of the label if possible, im happy if you come up with your own shield designs.

Target Market(s)

Mechanics

Industry/Entity Type

Automotive Part

Requirements
Must have
• My logo on top
Nice to have
• Silver background
Should not have
• Pictures of engines or engine parts etc

```html
<!DOCTYPE html>
<html lang="en">
<head>
<meta charset="utf-8">
<title>Torlux Motor Clear &amp; Renew – Label</title>
<link rel="stylesheet" href="https://fonts.googleapis.com/css2?family=Oswald:wght@400;500&family=Russo+One&family=Roboto:wght@400;700&display=swap">
<style>
  :root{
    --stage:#ffffff;
    --silver-light:#f4f5f7;
    --silver-mid:#d9dde3;
    --silver-dark:#aeb4bd;
    --blue-deep:#0f3f8c;
    --blue:#1f64c4;
    --blue-bright:#3b8ee6;
    --blue-pale:#9cc8f2;
    --orange:#f07a1a;
    --orange-dark:#d85a0a;
    --white:#ffffff;
    --ink:#14306b;
  }
  *{box-sizing:border-box;margin:0;padding:0}
  html,body{width:727px;height:1200px;overflow:hidden;background:var(--stage)}
  .canvas{position:relative;width:727px;height:1200px}
  .label{position:absolute;top:60px;width:300px;height:1080px;overflow:hidden;border-radius:4px;
    background:linear-gradient(90deg,var(--silver-dark) 0%,var(--silver-light) 35%,var(--white) 55%,var(--silver-mid) 100%)}
  .label--front{left:38px}
  .label--back{left:389px}
  .label__art{position:absolute;inset:0;width:100%;height:100%}
  .label__rim{position:absolute;left:0;right:0;height:10px;background:linear-gradient(180deg,var(--blue-bright),var(--blue-deep))}
  .label__rim--top{top:0}
  .label__rim--bottom{bottom:0}

  .brand{position:absolute;left:0;right:0;display:flex;align-items:center;justify-content:center;gap:10px}
  .brand__dot{width:22px;height:22px;border-radius:50%;background:var(--blue)}
  .brand__name{font-family:"Oswald",sans-serif;font-weight:500;color:var(--blue);letter-spacing:3px;text-transform:uppercase}
  .label--front .brand{top:90px}
  .label--front .brand__name{font-size:44px}
  .label--back .brand{top:50px}
  .label--back .brand__name{font-size:30px}

  .title{position:absolute;left:14px;top:250px;width:280px;transform:rotate(-8deg);transform-origin:left top;
    font-family:"Russo One",sans-serif;color:var(--blue);line-height:1;text-transform:uppercase}
  .title__line{display:block;font-size:40px}
  .title__line--second{font-size:40px;padding-left:10px}

  .banner{position:absolute;left:-20px;top:430px;width:360px;padding:10px 0 10px 40px;background:var(--orange);
    transform:rotate(-16deg);transform-origin:left top;font-family:"Russo One",sans-serif;color:var(--blue-deep);
    font-size:25px;line-height:1.05;text-transform:uppercase;text-align:center}

  .benefits{position:absolute;left:22px;top:660px;width:270px;list-style:none;font-family:"Oswald",sans-serif;
    color:var(--white);font-size:19px;letter-spacing:1px;line-height:1.6;text-transform:uppercase}
  .benefits li{position:relative;padding-left:20px}
  .benefits li::before{content:"";position:absolute;left:0;top:11px;width:8px;height:8px;border-radius:50%;background:var(--orange)}
  .volume{position:absolute;left:0;right:0;bottom:34px;text-align:center;font-family:"Oswald",sans-serif;color:var(--white);font-size:28px;letter-spacing:2px}

  .copy{position:absolute;left:18px;width:264px;font-family:"Roboto",sans-serif;color:var(--blue)}
  .copy__heading{font-weight:700;font-size:14px;margin-bottom:4px;color:var(--blue-deep)}
  .copy__body{font-size:8px;line-height:1.45;text-align:justify}
  .copy--application{top:150px}
  .copy--features{top:285px}
  .copy--directions{top:420px}

  .info{position:absolute;left:0;right:0;top:820px;text-align:center;font-family:"Roboto",sans-serif;color:var(--white);font-size:11px;line-height:1.7}
  .info strong{font-weight:700}
  .info__site{font-weight:700;font-size:12px}
  .info__warning{display:inline-block;margin-top:6px;font-weight:700;font-size:10px;border-left:1px solid var(--white);border-right:1px solid var(--white);padding:0 6px}
  .badges{position:absolute;left:0;right:0;bottom:34px;display:flex;justify-content:center;gap:10px}
  .badge{width:22px;height:22px;border-radius:50%;border:2px solid var(--white)}
</style>
</head>
<body>
<main class="canvas">

  <section class="label label--front" aria-label="Front label">
    <svg class="label__art" viewBox="0 0 300 1080" preserveAspectRatio="none" aria-hidden="true">
      <defs>
        <linearGradient id="front-blue" x1="0" y1="0" x2="1" y2="0">
          <stop offset="0" stop-color="#0f3f8c"/><stop offset="0.5" stop-color="#2a72cf"/><stop offset="1" stop-color="#174c9e"/>
        </linearGradient>
      </defs>
      <polygon points="0,330 300,250 300,290 0,380" fill="#3b8ee6" opacity="0.5"/>
      <polygon points="0,300 300,210 300,230 0,320" fill="#9cc8f2" opacity="0.6"/>
      <polygon points="0,420 300,360 300,1080 0,1080" fill="url(#front-blue)"/>
      <polygon points="0,420 300,360 300,380 0,445" fill="#9cc8f2"/>
      <polygon points="0,560 300,470 300,500 0,600" fill="#d85a0a"/>
    </svg>
    <div class="label__rim label__rim--top"></div>
    <div class="brand"><span class="brand__dot"></span><span class="brand__name">torlux</span></div>
    <h1 class="title"><span class="title__line">Motor Clear</span><span class="title__line title__line--second">&amp; Renew</span></h1>
    <p class="banner">Prepares engines<br>for new oil</p>
    <ul class="benefits">
      <li>Restores compression</li>
      <li>Minimises contamination with new oil</li>
      <li>Contains torlux armor coat protection</li>
      <li>Recommended for petrol, diesel and hybrid engines</li>
    </ul>
    <p class="volume">350ML</p>
    <div class="label__rim label__rim--bottom"></div>
  </section>

  <section class="label label--back" aria-label="Back label">
    <svg class="label__art" viewBox="0 0 300 1080" preserveAspectRatio="none" aria-hidden="true">
      <defs>
        <linearGradient id="back-blue" x1="0" y1="0" x2="1" y2="0">
          <stop offset="0" stop-color="#174c9e"/><stop offset="0.5" stop-color="#2a72cf"/><stop offset="1" stop-color="#0f3f8c"/>
        </linearGradient>
      </defs>
      <polygon points="0,600 300,700 300,1080 0,1080" fill="url(#back-blue)"/>
      <polygon points="0,585 300,690 300,705 0,605" fill="#9cc8f2"/>
      <polygon points="0,560 300,660 300,668 0,570" fill="#3b8ee6"/>
    </svg>
    <div class="label__rim label__rim--top"></div>
    <div class="brand"><span class="brand__dot"></span><span class="brand__name">torlux</span></div>

    <div class="copy copy--application">
      <h2 class="copy__heading">APPLICATION</h2>
      <p class="copy__body">Lorem Ipsum is simply dummy text of the printing and typesetting industry. Lorem Ipsum has been the industry's standard dummy text ever since the 1500s, when an unknown printer took a galley of type and scrambled it to make a type specimen book. It has survived not only five centuries, but also the leap into electronic typesetting, remaining essentially unchanged.</p>
    </div>
    <div class="copy copy--features">
      <h2 class="copy__heading">FEATURES:</h2>
      <p class="copy__body">Lorem Ipsum is simply dummy text of the printing and typesetting industry. Lorem Ipsum has been the industry's standard dummy text ever since the 1500s, when an unknown printer took a galley of type and scrambled it to make a type specimen book. It has survived not only five centuries, but also the leap into electronic typesetting, remaining essentially unchanged.</p>
    </div>
    <div class="copy copy--directions">
      <h2 class="copy__heading">DIRECTIONS:</h2>
      <p class="copy__body">Lorem Ipsum is simply dummy text of the printing and typesetting industry. Lorem Ipsum has been the industry's standard dummy text ever since the 1500s, when an unknown printer took a galley of type and scrambled it to make a type specimen book. It has survived not only five centuries, but also the leap into electronic typesetting, remaining essentially unchanged.</p>
    </div>

    <div class="info">
      <p>Visit our website:</p>
      <p class="info__site">www.torluxsupply.net.au</p>
      <p><strong>Validity :</strong> 3 years</p>
      <p><strong>Product date:</strong> Please see can Bottom</p>
      <p class="info__warning">KEEP OUT OF REACH OF CHILDREN</p>
    </div>
    <div class="badges"><span class="badge"></span><span class="badge"></span><span class="badge"></span></div>
    <div class="label__rim label__rim--bottom"></div>
  </section>

</main>
</body>
</html>
```